Flyer for a marketing

We are a holistic mental health facility in need of a flyer to help promote our services and encourage more people to seek care. See the attachment to tell you more. We prefer warm green colors or rich blue. Thank you.

```html
<!DOCTYPE html>
<html lang="en">
<head>
<meta charset="utf-8">
<title>Clearwater Behavioral Care – Flyer</title>
<link rel="stylesheet" href="https://fonts.googleapis.com/css2?family=Montserrat:wght@400;500;700&family=Oswald:wght@400;500&display=swap">
<style>
  :root {
    --page-bg: #c9c9c9;
    --navy: #0f3f78;
    --cyan: #1fb7ea;
    --cyan-light: #5fd0f5;
    --ink: #17223b;
    --white: #ffffff;
    --green: #1f9d55;
  }
  * { box-sizing: border-box; margin: 0; padding: 0; }
  html, body { width: 1200px; height: 1200px; overflow: hidden; background: var(--page-bg); }
  .flyer {
    position: absolute; left: 225px; top: 44px;
    width: 750px; height: 1112px;
    background: var(--navy);
    overflow: hidden;
    font-family: "Montserrat", Arial, sans-serif;
    color: var(--white);
  }
  .flyer-art { position: absolute; inset: 0; }
  .brand {
    position: absolute; left: 48px; top: 96px;
    display: flex; align-items: center; gap: 18px;
  }
  .brand-mark { width: 44px; height: 44px; border-radius: 50%; background: var(--cyan); flex: none; }
  .brand-name {
    font-family: "Montserrat", Arial, sans-serif; font-weight: 700;
    font-size: 22px; line-height: 26px; color: var(--navy);
  }
  .intro { position: absolute; left: 0; right: 0; top: 507px; text-align: center; }
  .intro-tagline { color: var(--cyan); font-weight: 700; font-size: 26px; line-height: 30px; }
  .intro-lead { font-size: 25px; line-height: 30px; font-weight: 500; margin-top: 7px; }
  .intro-lead strong { font-weight: 700; }
  .section { position: absolute; left: 30px; right: 20px; }
  .section-title {
    font-family: "Oswald", "Arial Narrow", sans-serif; font-weight: 400;
    color: var(--cyan); font-size: 25px; line-height: 30px; text-transform: uppercase;
  }
  .section-body { font-size: 24px; line-height: 28px; font-weight: 500; margin-top: 6px; }
  .section--accepting { top: 643px; }
  .section--why { top: 767px; }
  .contact-tab {
    position: absolute; left: 0; top: 1014px; width: 222px; height: 32px;
    background: var(--cyan);
    clip-path: polygon(0 0, 190px 0, 222px 100%, 0 100%);
    font-family: "Oswald", "Arial Narrow", sans-serif; font-weight: 400;
    font-size: 21px; line-height: 32px; padding-left: 33px; letter-spacing: 0.8px;
    text-transform: uppercase;
  }
  .footer {
    position: absolute; left: 0; right: 0; bottom: 0; height: 66px;
    background: var(--white); border-top: 3px solid var(--green);
    font-family: "Oswald", "Arial Narrow", sans-serif; font-size: 13.5px;
    color: var(--ink); text-transform: uppercase;
  }
  .footer-company { position: absolute; left: 30px; top: 12px; color: var(--cyan); }
  .footer-address { position: absolute; left: 28px; top: 34px; letter-spacing: -0.35px; font-weight: 500; }
  .footer-line { position: absolute; display: flex; align-items: center; gap: 6px; font-weight: 500; }
  .footer-line svg { width: 14px; height: 14px; fill: var(--cyan); flex: none; }
  .footer-phone { left: 356px; top: 12px; }
  .footer-fax { left: 356px; top: 34px; }
  .footer-web { left: 492px; top: 12px; }
  .footer-mail { left: 492px; top: 34px; }
</style>
</head>
<body>
<main class="flyer">
  <svg class="flyer-art" viewBox="0 0 750 1112" width="750" height="1112">
    <defs>
      <linearGradient id="photoTone" x1="0" y1="0" x2="1" y2="0.3">
        <stop offset="0" stop-color="#f7f7f8"/>
        <stop offset="0.45" stop-color="#e4ddd8"/>
        <stop offset="0.75" stop-color="#b99a86"/>
        <stop offset="1" stop-color="#8d9bb3"/>
      </linearGradient>
      <linearGradient id="navyPanel" x1="0" y1="0" x2="0" y2="1">
        <stop offset="0" stop-color="#0c3a70"/>
        <stop offset="1" stop-color="#114683"/>
      </linearGradient>
    </defs>
    <rect x="0" y="0" width="750" height="520" fill="url(#photoTone)" role="img" aria-label="Photo of a smiling family of four sitting together on a sofa at home"/>
    <path d="M0,226 Q375,726 750,122" fill="none" stroke="#ffffff" stroke-width="4"/>
    <path d="M0,238 Q375,738 750,134 L750,190 Q375,760 0,252 Z" fill="var(--cyan)"/>
    <path d="M0,250 Q375,752 750,180 L750,1112 L0,1112 Z" fill="url(#navyPanel)"/>
    <path d="M560,420 Q680,330 750,190 L750,250 Q690,370 560,420 Z" fill="var(--cyan-light)" opacity="0.6"/>
  </svg>

  <header class="brand">
    <span class="brand-mark"></span>
    <p class="brand-name">Clearwater<br>Behavioral Care</p>
  </header>

  <section class="intro">
    <h2 class="intro-tagline">The Care You Deserve</h2>
    <p class="intro-lead"><strong>Clearwater Behavioral Care</strong>, where<br>deserving patients meet compassionate providers.</p>
  </section>

  <section class="section section--accepting">
    <h3 class="section-title">We are accepting new patients, no waiting list.</h3>
    <p class="section-body">Your mental health matters, so make it a priority and<br>call us today for an appointment.</p>
  </section>

  <section class="section section--why">
    <h3 class="section-title">Why choose us?</h3>
    <p class="section-body">We are an integrative holistic psychiatric center.<br>Our mission is to provide compassionate quality care.<br>We provide psychiatric services including medication<br>management and psychotherapy.<br>We listen, care, and empower you to live better.<br>We accept major insurances.</p>
  </section>

  <div class="contact-tab">Contact us</div>

  <footer class="footer">
    <p class="footer-company">Clearwater Behavioral Care, APNC</p>
    <p class="footer-address">4180 Maple Grove Road, Suite 210 - Fairview, CA 90000</p>
    <p class="footer-line footer-phone">
      <svg viewBox="0 0 24 24"><path d="M6.6 10.8a15.1 15.1 0 0 0 6.6 6.6l2.2-2.2c.3-.3.7-.4 1-.2 1.1.4 2.3.6 3.6.6.6 0 1 .4 1 1V20c0 .6-.4 1-1 1A17 17 0 0 1 3 4c0-.6.4-1 1-1h3.5c.6 0 1 .4 1 1 0 1.3.2 2.5.6 3.6.1.3 0 .7-.2 1z"/></svg>
      (555) 310-4827
    </p>
    <p class="footer-line footer-fax">
      <svg viewBox="0 0 24 24"><path d="M6 2h9v5H6zM3 8h18v13H3zm3 3v2h4v-2zm0 4v2h4v-2zm7-4v6h5v-6z"/></svg>
      (555) 310-4828
    </p>
    <p class="footer-line footer-web">
      <svg viewBox="0 0 24 24"><path d="M12 2a10 10 0 1 0 0 20 10 10 0 0 0 0-20zm6.9 6h-3a15 15 0 0 0-1.3-4A8 8 0 0 1 18.9 8zM12 4c.8 1.2 1.5 2.5 1.9 4h-3.8c.4-1.5 1.1-2.8 1.9-4zM4.3 14a8 8 0 0 1 0-4h3.4a16 16 0 0 0 0 4zm.8 2h3a15 15 0 0 0 1.3 4A8 8 0 0 1 5.1 16zm3-8h-3a8 8 0 0 1 4.3-4c-.6 1.2-1 2.6-1.3 4zM12 20c-.8-1.2-1.5-2.5-1.9-4h3.8c-.4 1.5-1.1 2.8-1.900 4zm2.3-6H9.7a14 14 0 0 1 0-4h4.6a14 14 0 0 1 0 4zm.3 6c.6-1.2 1-2.6 1.3-4h3a8 8 0 0 1-4.3 4zm1.7-6a16 16 0 0 0 0-4h3.4a8 8 0 0 1 0 4z"/></svg>
      clearwaterbehavioral.com
    </p>
    <p class="footer-line footer-mail">
      <svg viewBox="0 0 24 24"><path d="M2 5h20v14H2zm2 2v.5l8 5 8-5V7l-8 5z"/></svg>
      info@clearwaterbehavioral.com
    </p>
  </footer>
</main>
</body>
</html>
```